BriVento Powerpoint design

We've recently redesigned our logos and would like a single presentation format that we can easily interchange the logos attached into. The presentation will be used for general company sales information. The group is called BriVento and has 2 companies, k7wavesystems and Quiet Bridge. We're an IT services company who specialises in Broadband and general network services.

Target Market(s)

Professional

```html
<!DOCTYPE html>
<html lang="en">
<head>
<meta charset="utf-8">
<title>BriVento Group – Presentation</title>
<link href="https://fonts.googleapis.com/css2?family=Poppins:wght@400;500;600;700&family=Sen:wght@700;800&display=swap" rel="stylesheet">
<style>
:root{
  --page:#2f3532;
  --ink:#111111;
  --text:#2a2a2a;
  --white:#ffffff;
  --blue:#29a3dc;
  --green:#0a6b35;
  --red:#d0111b;
  --lime:#8bc43f;
  --mint:#e3efe7;
}
*{margin:0;padding:0;box-sizing:border-box}
html,body{width:1200px;height:3981px;overflow:hidden;background:var(--page)}
body{position:relative;font-family:"Poppins",sans-serif;color:var(--text)}
.slide{position:absolute;left:39px;width:1123px;background:var(--white);overflow:hidden}
.slide > *{position:absolute}
.stripe{left:0;bottom:0;width:100%;height:7px;display:flex}
.stripe span{height:100%}
.stripe .s1{width:275px;background:var(--blue)}
.stripe .s2{width:274px;background:var(--green)}
.stripe .s3{width:297px;background:var(--red)}
.stripe .s4{flex:1;background:var(--lime)}
.dots{display:flex;gap:8px}
.dots i{width:17px;height:17px;border-radius:50%;display:block}
.dots i:nth-child(1){background:var(--green)}
.dots i:nth-child(2){background:var(--blue)}
.dots i:nth-child(3){background:var(--lime)}
.dots i:nth-child(4){background:var(--red)}
.title{font-family:"Sen",sans-serif;font-weight:800;color:var(--ink);font-size:50px;line-height:1}
.subtitle{font-size:18px;color:var(--text)}
.logo{display:flex;align-items:center;gap:12px;font-family:"Poppins",sans-serif;font-weight:600;color:var(--ink);white-space:nowrap}
.logo .mark{border-radius:50%;background:var(--green);flex:none}
.logo-head{right:56px;top:30px;font-size:52px}
.logo-head .mark{width:50px;height:50px}
.brands{display:flex;gap:22px;font-weight:500;font-size:25px;color:var(--ink);white-space:nowrap}
.brand{display:flex;align-items:center;gap:8px}
.brand .mark{width:22px;height:22px;border-radius:50%;flex:none}
.mark.b{background:var(--blue)}
.mark.r{background:var(--red)}
.photo{border-radius:22px;overflow:hidden}

/* cover */
.cover{top:39px;height:629px;background:#0e1216}
.cover .bg{inset:0;background:radial-gradient(ellipse at 60% 40%,#2a3a40 0%,#141c20 45%,#07090b 100%)}
.cover .logo{left:66px;top:268px;font-size:76px;color:var(--white)}
.cover .logo .mark{width:70px;height:70px;background:var(--white)}
.cover .divider{left:560px;top:126px;width:2px;height:376px;background:#cfcfcf}
.cover .dots{left:624px;top:162px}
.cover .welcome{left:622px;top:196px;font-family:"Sen",sans-serif;font-weight:800;color:var(--white);font-size:54px;line-height:1.2;white-space:nowrap}
.cover .tag{left:624px;top:340px;color:var(--white);font-size:17px}
.cover .brands{left:624px;top:374px;color:var(--white);font-size:20px;gap:18px}
.cover .brand .mark{width:24px;height:24px;background:var(--white)}
.social{left:624px;top:424px;display:flex;gap:14px}
.social i{display:block;width:40px;height:40px;border-radius:50%;border:2px solid var(--white)}

/* about */
.about{top:693px;height:632px}
.about .dots,.services .dots,.process .dots,.gallery .dots{left:57px;top:24px}
.about .title,.services .title,.process .title,.gallery .title{left:57px;top:52px}
.about .subtitle,.services .subtitle,.process .subtitle,.gallery .subtitle{left:57px;top:110px}
.about .band{left:0;top:173px;width:560px;height:65px;background:var(--mint)}
.about .band-label{left:0;top:185px;width:505px;text-align:right;font-weight:600;font-size:28px;color:var(--green)}
.about .copy{left:57px;top:255px;width:455px;font-size:17px;line-height:37.5px;text-align:justify}
.about .photo{left:535px;top:134px;width:532px;height:430px;background:linear-gradient(135deg,#4b5a63 0%,#2b3338 55%,#1a1f22 100%)}
.about .caption{left:535px;top:490px;width:532px;height:74px;border-radius:0 0 22px 22px;background:rgba(20,24,26,.75);color:var(--white);font-weight:600;font-size:23px;text-align:center;line-height:74px}
.about .brands,.process .brands{left:57px;top:560px}

/* services grid */
.services{top:1348px;height:631px}
.services .dark{left:0;top:0;width:1123px;height:631px}
.svc{width:270px;text-align:center;top:198px}
.svc .ring{width:150px;height:150px;margin:0 auto;border-radius:50%;background:var(--white);display:flex;align-items:center;justify-content:center}
.svc .disc{width:130px;height:130px;border-radius:50%;display:flex;align-items:center;justify-content:center}
.svc p{margin-top:18px;color:var(--white);font-size:17.5px;line-height:35.5px}
.services .brands{left:57px;top:572px}
.services .brand{background:var(--white);padding:0 4px}

/* process */
.process{top:2004px;height:629px}
.process .laptop{left:57px;top:219px;width:430px;height:236px;border-radius:10px;background:linear-gradient(180deg,#2a2a2a 0%,#dcdcdc 8%,#f2f2f2 85%,#3a3a3a 100%)}
.step-icon{width:118px;height:118px;border-radius:50%;background:var(--white);box-shadow:0 4px 10px rgba(0,0,0,.25);display:flex;align-items:center;justify-content:center}
.step-icon .disc{width:100px;height:100px;border-radius:50%;display:flex;align-items:center;justify-content:center}
.step{width:390px}
.step h3{font-size:18px;font-weight:600;color:var(--ink);line-height:28px}
.step p{font-size:16px;line-height:35px;color:var(--text)}
.connector{stroke:#333;stroke-width:1.5;stroke-dasharray:4 5;fill:none}

/* gallery */
.gallery{top:2659px;height:630px}
.gallery .photo{background:linear-gradient(135deg,#3d5566,#16212b)}
.gallery .brands{left:57px;top:585px;font-size:21px}

/* contact */
.contact{top:3313px;height:629px}
.contact .dots{left:57px;top:30px}
.contact .title{left:57px;top:62px}
.contact-row{left:57px;display:flex;align-items:center;gap:14px;font-size:20px;color:var(--ink)}
.contact-row .ic{width:46px;height:46px;border-radius:50%;display:flex;align-items:center;justify-content:center}
.contact .brands{left:57px;top:385px;flex-direction:column;gap:30px;font-size:42px}
.contact .brand .mark{width:40px;height:40px}
.contact .logo{left:505px;top:272px;font-size:86px;gap:20px}
.contact .logo .mark{width:96px;height:96px}
</style>
</head>
<body>

<section class="slide cover">
  <div class="bg" role="img" aria-label="Dark server room corridor with glowing rack lights"></div>
  <div class="logo"><span class="mark"></span>BriVento</div>
  <div class="divider"></div>
  <div class="dots"><i></i><i></i><i></i><i></i></div>
  <h1 class="welcome">Welcome To<br>BriVento Group</h1>
  <p class="tag">Lorem ipsum dolor sit amet</p>
  <div class="brands"><span class="brand"><span class="mark"></span>k7wavesystems</span><span class="brand"><span class="mark"></span>Quiet Bridge</span></div>
  <div class="social" aria-label="Social channels"><i></i><i></i><i></i><i></i></div>
</section>

<section class="slide about">
  <div class="dots"><i></i><i></i><i></i><i></i></div>
  <h2 class="title">About Us</h2>
  <p class="subtitle">Lorem ipsum dolor sit amet</p>
  <div class="logo logo-head"><span class="mark"></span>BriVento</div>
  <div class="band"></div>
  <div class="band-label">BriVento</div>
  <p class="copy">Lorem ipsum dolor sit amet, consectetur adipiscing elit, sed do eiusmod tempor incididunt ut labore et dolore magna aliqua. Ut enim ad minim veniam, quis nostrud exercitation ullamco laboris nisi ut aliquip ex ea commodo consequat. Duis reprehenderit in voluptate cupidatat non proident, sunt in culpa qui officia deserunt mollit anim id est laborum.</p>
  <div class="photo" role="img" aria-label="IT professional working at a computer with code on screens"></div>
  <div class="caption">IT services</div>
  <div class="brands"><span class="brand"><span class="mark b"></span>Quiet Bridge</span><span class="brand"><span class="mark r"></span>k7wavesystems</span></div>
  <div class="stripe"><span class="s1"></span><span class="s2"></span><span class="s3"></span><span class="s4"></span></div>
</section>

<section class="slide services">
  <svg class="dark" viewBox="0 0 1123 631" role="img" aria-label="Dark technology backdrop">
    <defs><linearGradient id="darkband" x1="0" y1="0" x2="1" y2="1"><stop offset="0" stop-color="#1b1f22"/><stop offset="1" stop-color="#050607"/></linearGradient></defs>
    <polygon points="0,245 560,205 1123,285 1123,631 0,631" fill="url(#darkband)"/>
  </svg>
  <div class="dots"><i></i><i></i><i></i><i></i></div>
  <h2 class="title">Our Services</h2>
  <p class="subtitle">Lorem ipsum dolor sit amet</p>
  <div class="logo logo-head"><span class="mark"></span>BriVento</div>

  <div class="svc" style="left:15px"><div class="ring"><div class="disc" style="background:var(--blue)"><svg width="66" height="60" viewBox="0 0 66 60" fill="none" stroke="#fff" stroke-width="3"><rect x="4" y="4" width="58" height="38" rx="3"/><path d="M33 42v8M20 54h26"/><circle cx="26" cy="23" r="7"/><path d="M38 23h14"/></svg></div></div><p>Lorem ipsum dolor sit amet, consectetur adipiscing elit, sed do eiusmod tempor incididunt ut labore et dolore magna aliqua.</p></div>
  <div class="svc" style="left:289px"><div class="ring"><div class="disc" style="background:var(--green)"><svg width="66" height="60" viewBox="0 0 66 60" fill="none" stroke="#fff" stroke-width="3"><rect x="4" y="4" width="58" height="38" rx="3"/><path d="M33 42v8M20 54h26"/><circle cx="26" cy="23" r="7"/><path d="M38 23h14"/></svg></div></div><p>Lorem ipsum dolor sit amet, consectetur adipiscing elit, sed do eiusmod tempor incididunt ut labore et dolore magna aliqua.</p></div>
  <div class="svc" style="left:564px"><div class="ring"><div class="disc" style="background:var(--red)"><svg width="66" height="60" viewBox="0 0 66 60" fill="none" stroke="#fff" stroke-width="3"><rect x="4" y="4" width="58" height="38" rx="3"/><path d="M33 42v8M20 54h26"/><circle cx="26" cy="23" r="7"/><path d="M38 23h14"/></svg></div></div><p>Lorem ipsum dolor sit amet, consectetur adipiscing elit, sed do eiusmod tempor incididunt ut labore et dolore magna aliqua.</p></div>
  <div class="svc" style="left:838px"><div class="ring"><div class="disc" style="background:var(--lime)"><svg width="66" height="60" viewBox="0 0 66 60" fill="none" stroke="#fff" stroke-width="3"><rect x="4" y="4" width="58" height="38" rx="3"/><path d="M33 42v8M20 54h26"/><circle cx="26" cy="23" r="7"/><path d="M38 23h14"/></svg></div></div><p>Lorem ipsum dolor sit amet, consectetur adipiscing elit, sed do eiusmod tempor incididunt ut labore et dolore magna aliqua.</p></div>

  <div class="brands"><span class="brand"><span class="mark b"></span>Quiet Bridge</span><span class="brand"><span class="mark r"></span>k7wavesystems</span></div>
  <div class="stripe"><span class="s1"></span><span class="s2"></span><span class="s3"></span><span class="s4"></span></div>
</section>

<section class="slide process">
  <div class="dots"><i></i><i></i><i></i><i></i></div>
  <h2 class="title">Our Services</h2>
  <p class="subtitle">Lorem ipsum dolor sit amet</p>
  <div class="logo logo-head"><span class="mark"></span>BriVento</div>
  <div class="laptop" role="img" aria-label="Laptop displaying the company name on screen"></div>
  <svg style="left:480px;top:150px" width="200" height="420" viewBox="0 0 200 420"><path class="connector" d="M50 20 L90 40"/><path class="connector" d="M130 110 L138 150"/><path class="connector" d="M130 270 L120 312"/><path class="connector" d="M50 400 L88 386"/></svg>
  <div class="step-icon" style="left:531px;top:140px"><div class="disc" style="background:var(--lime)"><svg width="52" height="52" viewBox="0 0 52 52" fill="none" stroke="#fff" stroke-width="3"><circle cx="26" cy="26" r="9"/><circle cx="26" cy="26" r="18" stroke-dasharray="6 4"/></svg></div></div>
  <div class="step" style="left:646px;top:152px"><h3>Lorem ipsum</h3><p>Lorem ipsum dolor sit amet, consectetur adipiscing elit, sed do eiusmod ut labore aliqua.</p></div>
  <div class="step-icon" style="left:541px;top:290px"><div class="disc" style="background:var(--blue)"><svg width="52" height="48" viewBox="0 0 52 48" fill="none" stroke="#fff" stroke-width="3"><rect x="3" y="3" width="46" height="30" rx="3"/><path d="M26 33v7M16 44h20"/><circle cx="20" cy="18" r="6"/></svg></div></div>
  <div class="step" style="left:677px;top:305px"><h3>Lorem ipsum</h3><p>Lorem ipsum dolor sit amet, consectetur adipiscing elit, sed do eiusut labore et aliqua.</p></div>
  <div class="step-icon" style="left:511px;top:444px"><div class="disc" style="background:var(--red)"><svg width="52" height="52" viewBox="0 0 52 52" fill="none" stroke="#fff" stroke-width="3"><circle cx="26" cy="26" r="20"/><path d="M6 26h40M26 6v40M12 12l28 28M40 12L12 40"/></svg></div></div>
  <div class="step" style="left:646px;top:455px"><h3>Lorem ipsum</h3><p>Lorem ipsum dolor sit amet, consectetur adipiscing elit, sed do eiusmod tempor i aliqua.</p></div>
  <div class="brands"><span class="brand"><span class="mark b"></span>Quiet Bridge</span><span class="brand"><span class="mark r"></span>k7wavesystems</span></div>
  <div class="stripe"><span class="s1"></span><span class="s2"></span><span class="s3"></span><span class="s4"></span></div>
</section>

<section class="slide gallery">
  <div class="dots"><i></i><i></i><i></i><i></i></div>
  <h2 class="title">Our Gallery</h2>
  <p class="subtitle" style="top:108px">Lorem ipsum dolor sit amet</p>
  <div class="logo logo-head"><span class="mark"></span>BriVento</div>
  <div class="photo" style="left:57px;top:135px;width:320px;height:208px" role="img" aria-label="Hand touching floating data charts"></div>
  <div class="photo" style="left:402px;top:135px;width:320px;height:208px;background:linear-gradient(135deg,#6fc3f0,#0b3a66)" role="img" aria-label="Cloud computing concept over a laptop"></div>
  <div class="photo" style="left:745px;top:135px;width:322px;height:432px;background:linear-gradient(160deg,#c9b79c,#5a4a3a 60%,#2c2520)" role="img" aria-label="Engineer at a desk working with a computer"></div>
  <div class="photo" style="left:57px;top:356px;width:320px;height:211px;background:linear-gradient(135deg,#2e6a9a,#0c1f33)" role="img" aria-label="Technician with laptop in a data centre"></div>
  <div class="photo" style="left:402px;top:356px;width:320px;height:211px;background:linear-gradient(135deg,#1c1c22,#6b3a1a 60%,#e0782a)" role="img" aria-label="Hand touching a glowing network diagram"></div>
  <div class="brands"><span class="brand"><span class="mark b"></span>Quiet Bridge</span><span class="brand"><span class="mark r"></span>k7wavesystems</span></div>
  <div class="stripe"><span class="s1"></span><span class="s2"></span><span class="s3"></span><span class="s4"></span></div>
</section>

<section class="slide contact">
  <div class="dots"><i></i><i></i><i></i><i></i></div>
  <h2 class="title">Contact Us</h2>
  <div class="contact-row" style="top:138px"><span class="ic" style="background:var(--green)"><svg width="22" height="22" viewBox="0 0 24 24" fill="#fff"><path d="M6.6 10.8a15.1 15.1 0 006.6 6.6l2.2-2.2c.3-.3.7-.4 1-.2 1.1.4 2.3.6 3.6.6.6 0 1 .4 1 1V20c0 .6-.4 1-1 1C10.6 21 3 13.4 3 4c0-.6.4-1 1-1h3.5c.6 0 1 .4 1 1 0 1.3.2 2.5.6 3.6.1.3 0 .7-.2 1z"/></svg></span>+1 555 0142 7788</div>
  <div class="contact-row" style="top:211px"><span class="ic" style="background:var(--blue)"><svg width="22" height="18" viewBox="0 0 22 18" fill="none" stroke="#fff" stroke-width="2"><rect x="1" y="1" width="20" height="16" rx="2"/><path d="M1 3l10 7 10-7"/></svg></span>hello@briventogroup.example</div>
  <div class="contact-row" style="top:284px"><span class="ic" style="background:var(--red)"><svg width="18" height="24" viewBox="0 0 18 24" fill="#fff"><path d="M9 0a9 9 0 00-9 9c0 6.8 9 15 9 15s9-8.2 9-15a9 9 0 00-9-9zm0 12.5A3.5 3.5 0 119 5.5a3.5 3.5 0 010 7z"/></svg></span>BriVento Group, United State.</div>
  <div class="brands"><span class="brand"><span class="mark b"></span>Quiet Bridge</span><span class="brand"><span class="mark r"></span>k7wavesystems</span></div>
  <div class="logo"><span class="mark"></span>BriVento</div>
  <div class="stripe"><span class="s1"></span><span class="s2"></span><span class="s3"></span><span class="s4"></span></div>
</section>

</body>
</html>
```